Verdano Harvest - Stationery Design Project

We need a stationary for our business. We grow roots and fruits in Central and South America, we import and distribute in FL, USA. We do fresh and frozen products.

Target Market(s)

Small and big supermarkets, wholesalers, traders, distributors, etc

Industry/Entity Type

Business

```html
<!DOCTYPE html>
<html lang="en">
<head>
<meta charset="utf-8">
<title>Verdano Harvest – Stationery</title>
<link rel="stylesheet" href="https://fonts.googleapis.com/css2?family=Montserrat:wght@400;500&display=swap">
<style>
  :root {
    --canvas: #e6e6e4;
    --olive: #536232;
    --olive-soft: #62713f;
    --paper: #f8f8f7;
    --paper-shade: #efefea;
    --orange: #e8860f;
    --ink: #6b6b6b;
    --white: #ffffff;
  }
  * { box-sizing: border-box; margin: 0; padding: 0; }
  html, body { width: 1200px; height: 1000px; overflow: hidden; }
  body {
    background: var(--canvas);
    font-family: "Montserrat", Arial, sans-serif;
    position: relative;
  }
  .sheet { position: absolute; overflow: hidden; }
  .wordmark {
    position: absolute;
    font-weight: 500;
    text-transform: uppercase;
    letter-spacing: 0.02em;
    white-space: nowrap;
  }
  .corner-accent {
    position: absolute;
    border-radius: 50%;
  }

  /* Presentation folder */
  .folder { left: 190px; top: 108px; width: 385px; height: 542px; background: var(--olive); }
  .folder .wordmark { left: 0; right: 0; top: 56px; text-align: center; font-size: 21px; color: var(--white); }
  .folder .corner-accent { width: 300px; height: 300px; right: -90px; bottom: -120px; background: var(--olive-soft); }

  /* Letterhead */
  .letterhead { left: 610px; top: 122px; width: 375px; height: 528px; background: var(--paper); }
  .letterhead .wordmark { left: 20px; top: 38px; font-size: 14px; color: var(--orange); }
  .letterhead .corner-accent { width: 240px; height: 240px; right: -70px; bottom: -95px; background: var(--paper-shade); }
  .letterhead .footer-band { position: absolute; left: 0; right: 0; bottom: 0; height: 7px; background: var(--olive); }
  .contact { position: absolute; bottom: 20px; font-size: 6.5px; color: var(--ink); line-height: 10px; }
  .contact li { list-style: none; display: flex; align-items: center; gap: 6px; }
  .contact svg { width: 8px; height: 6px; fill: var(--olive); }
  .contact--phone { left: 17px; }
  .contact--web { left: 104px; }
  .contact-divider { position: absolute; left: 85px; bottom: 20px; width: 1px; height: 18px; background: #bdbdbd; }

  /* Envelope */
  .envelope { left: 190px; top: 698px; width: 392px; height: 192px; background: var(--paper); }
  .envelope .flap { position: absolute; left: 0; top: 0; width: 392px; height: 57px; }
  .envelope .wordmark { left: 0; right: 0; top: 21px; text-align: center; font-size: 12px; color: var(--white); }

  /* Compliment card */
  .compliment { left: 618px; top: 698px; width: 392px; height: 192px; background: var(--paper); }
  .compliment .wordmark { left: 31px; top: 25px; font-size: 11px; color: var(--orange); }
  .compliment .corner-accent { width: 150px; height: 150px; right: -45px; bottom: -55px; background: var(--paper-shade); }
  .compliment .footer-band { position: absolute; left: 0; right: 0; bottom: 0; height: 7px; background: var(--olive); }
</style>
</head>
<body>

  <section class="sheet folder" aria-label="Presentation folder">
    <div class="corner-accent" aria-hidden="true"></div>
    <div class="wordmark">Verdano Harvest</div>
  </section>

  <section class="sheet letterhead" aria-label="Letterhead">
    <div class="corner-accent" aria-hidden="true"></div>
    <div class="wordmark">Verdano Harvest</div>
    <ul class="contact contact--phone">
      <li><svg viewBox="0 0 8 6"><path d="M0 0 L8 3 L0 6 Z"/></svg>0491570156</li>
      <li><svg viewBox="0 0 8 6"><path d="M0 0 L8 3 L0 6 Z"/></svg>0491570110</li>
    </ul>
    <span class="contact-divider" aria-hidden="true"></span>
    <ul class="contact contact--web">
      <li><svg viewBox="0 0 8 6"><path d="M0 0 L8 3 L0 6 Z"/></svg>www.verdanoharvest.com</li>
      <li><svg viewBox="0 0 8 6"><path d="M0 0 L8 3 L0 6 Z"/></svg>support@verdanoharvest.com</li>
    </ul>
    <div class="footer-band"></div>
  </section>

  <section class="sheet envelope" aria-label="Envelope">
    <svg class="flap" viewBox="0 0 392 57" aria-hidden="true">
      <path d="M0 0 H392 V32 Q392 54 370 56 H22 Q0 54 0 32 Z" fill="var(--olive)"/>
    </svg>
    <div class="wordmark">Verdano Harvest</div>
  </section>

  <section class="sheet compliment" aria-label="Compliment slip">
    <div class="corner-accent" aria-hidden="true"></div>
    <div class="wordmark">Verdano Harvest</div>
    <div class="footer-band"></div>
  </section>

</body>
</html>
```